Brelton Services - Fast, Efficient and Gas Mainteance for Domestic, Commercial and Industrial clients

We are in the process of purchasing a new business and would like to get a new logo and business card.
Business is a gas maintenance business that also does new gas installations.
Has been established since 1988.
Services include:
Install all types of gas appliances & equipment inc. hot water units
Maintain / repair / replace all types of gas appliances & equipment

Target Market(s)

Domestic, Commercial and Industrial clients

Industry/Entity Type

Business

Contact Information for Business Card

admin@breltonservices.example.au
07 5382 4690
Brelton Services PTY LTD

Logo Text

Gas Fitting & Plumbing Maintenance Specialists

Font styles to use
Sans Serif

Requirements
Must have
• Logo
• Business name, contact number, email address, web address
• Domestic | Commercial | Industrial Est Since 1988
Nice to have
• Possibly a black card with a flame logo to one side
Should not have
• Spelling errors

```html
<!DOCTYPE html>
<html lang="en">
<head>
<meta charset="utf-8">
<title>Brelton Services – Business Card</title>
<link rel="stylesheet" href="https://fonts.googleapis.com/css2?family=Arimo:wght@400;700&display=swap">
<style>
  :root {
    --backdrop: #ece8e2;
    --card-dark: #2a2a2c;
    --accent-orange: #f08a2a;
    --accent-yellow: #f6b332;
    --gradient-top: #f48a2e;
    --gradient-bottom: #fdc52c;
    --ink-dark: #3a2a14;
    --bar-dark: #2a2a2c;
  }
  * { margin: 0; padding: 0; box-sizing: border-box; }
  html, body {
    width: 1200px;
    height: 569px;
    overflow: hidden;
    background: var(--backdrop);
    font-family: "Arimo", Arial, sans-serif;
  }
  .stage { position: relative; width: 1200px; height: 569px; }
  .card {
    position: absolute;
    top: 166px;
    width: 402px;
    height: 236px;
    border-radius: 10px;
    overflow: hidden;
    box-shadow: 0 3px 8px rgba(0,0,0,0.25);
  }
  .card-front { left: 174px; background: var(--card-dark); }
  .card-back {
    left: 624px;
    background: linear-gradient(180deg, var(--gradient-top) 0%, var(--gradient-bottom) 100%);
  }
  .edge-bar {
    position: absolute;
    left: 0;
    top: 177px;
    width: 5px;
    height: 30px;
  }
  .card-front .edge-bar { background: linear-gradient(180deg, var(--accent-yellow), var(--accent-orange)); }
  .card-back .edge-bar { background: var(--bar-dark); }

  .brand {
    position: absolute;
    left: 48px;
    top: 56px;
    display: flex;
    flex-direction: column;
    align-items: flex-start;
    gap: 12px;
  }
  .brand-dot {
    width: 30px;
    height: 30px;
    border-radius: 50%;
    background: var(--accent-orange);
    margin-left: 40px;
  }
  .brand-name {
    font-size: 17px;
    font-weight: 700;
    letter-spacing: 0.5px;
    color: var(--accent-orange);
  }
  .sectors {
    position: absolute;
    left: 50px;
    top: 185px;
    font-size: 9.5px;
    line-height: 12px;
    color: var(--accent-yellow);
  }

  .contact-list {
    position: absolute;
    left: 27px;
    top: 174px;
    list-style: none;
    font-size: 10px;
    color: var(--ink-dark);
  }
  .contact-list li {
    display: flex;
    align-items: center;
    height: 15px;
  }
  .contact-list .company { margin-top: 3px; }
  .contact-icon {
    width: 10px;
    height: 10px;
    margin-right: 7px;
    flex: none;
  }
  .icon-spacer { width: 10px; margin-right: 7px; flex: none; }
</style>
</head>
<body>
<main class="stage">
  <section class="card card-front" aria-label="Card front">
    <div class="brand">
      <span class="brand-dot"></span>
      <span class="brand-name">Brelton Services</span>
    </div>
    <span class="edge-bar"></span>
    <p class="sectors">· Domestic &nbsp;· Commercial<br>· Industrial Est Since 1988</p>
  </section>

  <section class="card card-back" aria-label="Card back">
    <span class="edge-bar"></span>
    <ul class="contact-list">
      <li>
        <svg class="contact-icon" viewBox="0 0 10 10" aria-hidden="true">
          <rect x="0.5" y="2" width="9" height="6.5" fill="none" stroke="#3a2a14" stroke-width="1"/>
          <path d="M0.5 2 L5 5.8 L9.5 2" fill="none" stroke="#3a2a14" stroke-width="1"/>
        </svg>
        admin@breltonservices.example.au
      </li>
      <li>
        <svg class="contact-icon" viewBox="0 0 10 10" aria-hidden="true">
          <rect x="2.5" y="0.5" width="5" height="9" rx="0.8" fill="none" stroke="#3a2a14" stroke-width="1"/>
          <line x1="4.2" y1="8" x2="5.8" y2="8" stroke="#3a2a14" stroke-width="0.8"/>
        </svg>
        07 5382 4690
      </li>
      <li class="company"><span class="icon-spacer"></span>Brelton Services PTY LTD</li>
    </ul>
  </section>
</main>
</body>
</html>
```